CHIP BAG AND LOGO DESIGN - A salty snack that is focused on taste and texture

I need a logo and label design for our new brand "Vexamba". A salty snack that brings corn tortilla with extreme spices to excite the taste. First Flavor will be 'Trueno Pimienta and Kiwi'. Looking for a label design and a logo design for the Brand 'Vexamba'. This brand will have multiple types of snacks and all with different flavors and heat levels.

Target Market(s)

10- 25 year old

Industry/Entity Type

Salty Snacks

Font styles to use
Sans Serif
Other font styles liked:
• Arial, Bauhaus 93, Berlin Sans FB Demi, Cooper Black

Colors
59FF00
82FF00
B8FF75
E3FFCB
F4FFEA
FFF300
FFF600
FEFA6F
FFFEC7
FFFEE8
FFC000
F8CF3A
FAE287
FDF2CF
FEFAEE
F0912C
F2A743
F7CA91
FBE8D2
FDF5EE
EE7325
F08F49
F5BC92
FAE3D3
FDF4ED
EB3D1F
EC4F4E
F09395
F8D3D4
FCEDEE

Requirements
Must have
• Colors and design that pops, need the bags to jump off the shelf in a sea of competitors. I gave an example of Walrus Flax, I appreciate the artwork and design they did to differentiate their brand from others and appeal to the 10-25 demographics.
Nice to have
• Abstract / Cartoon like characteristics that speak of a south of the border recipe and origin. I would like to have in subtle grey or black background design much like the Aztec calendar that fills the space on a bag and/or a variation of that kind of design. In the front I'd like a character (maybe a warrior) of the same fashion. The logo (also being designed - "VEXAMBA") carefully blended into the artwork. Bold, Loud, jumps off the shelf with bright colors and graphics.
Should not have
• bland, boring, blah colors and designs. Should be fun and loud.

```html
<!DOCTYPE html>
<html lang="en">
<head>
<meta charset="utf-8">
<title>Vexamba – Trueno Pimienta and Kiwi</title>
<link rel="stylesheet" href="https://fonts.googleapis.com/css2?family=Montserrat:wght@700;800;900&family=Permanent+Marker&display=swap">
<style>
  :root {
    --stage: #8c8c8c;
    --leaf-dark: #2f7d2c;
    --leaf: #3f9a3a;
    --leaf-light: #5cb045;
    --calendar: #2b6f28;
    --corn: #e3c30a;
    --corn-pale: #f4f1b3;
    --sun: #fff300;
    --flavor-box: #7db33f;
    --ink: #111111;
    --paper: #ffffff;
    --fire: #f0912c;
    --fire-deep: #ee7325;
    --kiwi: #82ff00;
    --tag-med: #f2a743;
    --tag-low: #7cc12a;
    --tag-high: #c8103c;
  }
  * { box-sizing: border-box; margin: 0; padding: 0; }
  html, body { width: 1056px; height: 1200px; overflow: hidden; }
  body {
    background: var(--stage);
    font-family: "Montserrat", Arial, sans-serif;
    position: relative;
  }
  .bag-face {
    position: absolute;
    left: 145px; top: 36px;
    width: 766px; height: 1128px;
    overflow: hidden;
    background: linear-gradient(180deg, var(--corn) 55%, var(--corn-pale) 100%);
  }
  .bag-face > * { position: absolute; }
  .green-field { left: 0; top: 0; width: 766px; height: 720px; }
  .calendar-art {
    left: 61px; top: -67px; width: 646px; height: 646px;
    border-radius: 50%;
    background: radial-gradient(circle, var(--leaf-light) 0 30%, var(--calendar) 31% 100%);
    opacity: .85;
  }
  .new-badge {
    left: 506px; top: 48px; width: 220px; height: 150px;
    background: var(--sun);
    transform: rotate(-8deg);
    clip-path: polygon(4% 18%, 100% 0, 96% 82%, 0 100%);
    display: flex; align-items: center; justify-content: center;
  }
  .new-badge span {
    font-family: "Permanent Marker", cursive;
    font-size: 92px; color: var(--ink); line-height: 1;
  }
  .brand-name {
    left: 0; top: 392px; width: 766px;
    text-align: center;
    font-weight: 900; font-size: 132px; letter-spacing: 2px;
    color: var(--fire); line-height: 1;
  }
  .flavor-panel { left: 100px; top: 600px; width: 500px; height: 175px; transform: rotate(-4deg); }
  .flavor-panel .box { position: absolute; background: var(--flavor-box); border: 3px solid var(--ink); }
  .flavor-panel .box-top { left: 0; top: 0; width: 270px; height: 80px; }
  .flavor-panel .box-main { left: 125px; top: 40px; width: 360px; height: 130px; }
  .flavor-name {
    position: absolute; left: 10px; top: 0;
    font-weight: 900; color: var(--ink); line-height: .95;
    text-shadow: 3px 3px 0 var(--paper), -2px -2px 0 var(--paper), 2px -2px 0 var(--paper), -2px 2px 0 var(--paper);
  }
  .flavor-name .line { display: block; }
  .flavor-name .l1 { font-size: 58px; }
  .flavor-name .l2 { font-size: 58px; padding-left: 150px; }
  .flavor-name .l3 { font-size: 58px; padding-left: 132px; }
  .flavor-name .small { font-size: 32px; }
  .flame-kiwi-art {
    left: 451px; top: 640px; width: 290px; height: 370px;
    border-radius: 40% 40% 30% 30%;
    background: radial-gradient(ellipse at 55% 75%, var(--kiwi) 0 28%, transparent 46%),
                linear-gradient(180deg, var(--fire) 0%, var(--fire-deep) 60%, #f7ca91 100%);
    opacity: .85;
  }
  .nutrition { left: 34px; top: 948px; display: flex; gap: 2px; }
  .tag {
    width: 70px; height: 137px; border-radius: 22px;
    display: flex; flex-direction: column; align-items: center; overflow: hidden;
    font-weight: 700;
  }
  .tag .level { height: 28px; font-size: 17px; line-height: 28px; color: #5a3a00; }
  .tag .body {
    background: var(--paper); width: 60px; flex: 1;
    display: flex; flex-direction: column; align-items: center; justify-content: center;
    color: #333;
  }
  .tag .what { font-size: 12px; }
  .tag .amount { font-size: 20px; margin-top: 6px; }
  .tag .pct { height: 40px; font-size: 21px; line-height: 40px; color: #5a3a00; }
  .tag.med { background: var(--tag-med); }
  .tag.low { background: var(--tag-low); }
  .tag.high { background: var(--tag-high); }
  .tag.high .level, .tag.high .pct { color: #f8d3d4; }
  .weight {
    left: 549px; top: 1030px;
    font-weight: 900; font-size: 50px; color: var(--paper);
    text-shadow: 3px 3px 0 var(--ink), -3px -3px 0 var(--ink), 3px -3px 0 var(--ink), -3px 3px 0 var(--ink);
  }
  .net { left: 560px; top: 1092px; font-size: 13px; font-weight: 700; color: #444; }
</style>
</head>
<body>
  <main class="bag-face">
    <svg class="green-field" viewBox="0 0 766 720" aria-hidden="true">
      <defs>
        <linearGradient id="leafGrad" x1="0" y1="0" x2="0" y2="1">
          <stop offset="0" stop-color="#2f7d2c"/>
          <stop offset="1" stop-color="#4da53c"/>
        </linearGradient>
      </defs>
      <polygon points="0,0 766,0 766,590 430,640 0,700" fill="url(#leafGrad)"/>
    </svg>
    <div class="calendar-art" role="img" aria-label="Aztec sun calendar pattern in dark green line art"></div>
    <div class="new-badge"><span>NEW</span></div>
    <h1 class="brand-name">VEXAMBA</h1>
    <div class="flame-kiwi-art" role="img" aria-label="Orange flames rising behind sliced kiwi"></div>
    <div class="flavor-panel">
      <div class="box box-top"></div>
      <div class="box box-main"></div>
      <h2 class="flavor-name">
        <span class="line l1">Trueno</span>
        <span class="line l2">Pimienta</span>
        <span class="line l3"><span class="small">and</span> Kiwi</span>
      </h2>
    </div>
    <div class="nutrition">
      <div class="tag med"><span class="level">MED</span><div class="body"><span class="what">Calories</span><span class="amount">353</span></div><span class="pct">18%</span></div>
      <div class="tag low"><span class="level">LOW</span><div class="body"><span class="what">Sugar</span><span class="amount">0.9g</span></div><span class="pct">1%</span></div>
      <div class="tag med"><span class="level">MED</span><div class="body"><span class="what">Fat</span><span class="amount">20.3g</span></div><span class="pct">29%</span></div>
      <div class="tag high"><span class="level">HIGH</span><div class="body"><span class="what">Sat Fat</span><span class="amount">10.8g</span></div><span class="pct">54%</span></div>
      <div class="tag med"><span class="level">MED</span><div class="body"><span class="what">Salt</span><span class="amount">1.1g</span></div><span class="pct">18%</span></div>
    </div>
    <p class="weight">180g</p>
    <p class="net">Cont. Net.</p>
  </main>
</body>
</html>
```